Electrical Contracting Business card design

I would like a business card design for a new electrical business. I would like the print R.MOLT ELECTRICAL in large block lettering (spot gloss) on the front with atoms flying in a circle around the letter "A" of R.MOLT. Dark blue background, red lettering with the southern cross stars splashed in between the background and lettering.

On the rear of the card I would like the centre to have a box with 2 or 3 lines in it ( a space to write a time and date for the job to take place) surrounded by a big mass of confusing looking cables or a circuit diagram (something that would overwhelm people trying to make sense of it).

Thank you, I hope this isn't to detailed

Industry/Entity Type

Electrical

Contact Information for Business Card

R.MOLT ELECTRICAL
Phone: Brenn 0417853302
Brennr@mailvista.example
EC:47063

```html
<!DOCTYPE html>
<html lang="en">
<head>
<meta charset="utf-8">
<title>R.MOLT ELECTRICAL – Business Card</title>
<link rel="stylesheet" href="https://fonts.googleapis.com/css2?family=PT+Sans:wght@400;700&family=Alegreya+Sans:wght@400&display=swap">
<style>
  :root {
    --page-bg: #ffffff;
    --navy-deep: #05061f;
    --navy-mid: #1b1d3e;
    --navy-glow: #43455f;
    --swirl-tone: #2c2f55;
    --brand-red: #e3191f;
    --circuit-dark: #0d1422;
    --circuit-blue: #3f5a8a;
    --circuit-light: #8ea2c8;
    --panel-glass: rgba(215, 218, 232, 0.55);
    --panel-edge: rgba(255, 255, 255, 0.7);
    --field-white: #ffffff;
  }
  * { margin: 0; padding: 0; box-sizing: border-box; }
  html, body {
    width: 1200px;
    height: 1000px;
    overflow: hidden;
    background: var(--page-bg);
  }
  .canvas {
    position: relative;
    width: 1200px;
    height: 1000px;
  }

  /* Front of card */
  .card-front {
    position: absolute;
    left: 271px;
    top: 98px;
    width: 658px;
    height: 407px;
    overflow: hidden;
    background:
      radial-gradient(ellipse 300px 230px at 130px 245px, var(--navy-glow) 0%, var(--navy-mid) 55%, transparent 100%),
      linear-gradient(160deg, var(--navy-deep) 0%, #101230 60%, var(--navy-deep) 100%);
  }
  .card-front .swirl-art {
    position: absolute;
    right: 0;
    top: 0;
    width: 330px;
    height: 407px;
    background: radial-gradient(ellipse 260px 320px at 70% 55%, var(--swirl-tone) 0%, rgba(28, 30, 66, 0.6) 55%, transparent 100%);
  }
  .front-brand {
    position: absolute;
    right: 32px;
    top: 50px;
    font-family: "PT Sans", sans-serif;
    font-weight: 400;
    font-size: 50px;
    line-height: 1;
    letter-spacing: -0.5px;
    color: var(--brand-red);
    white-space: nowrap;
  }
  .contact-block {
    position: absolute;
    left: 27px;
    top: 268px;
    font-family: "Alegreya Sans", sans-serif;
    font-size: 24px;
    line-height: 27px;
    color: var(--brand-red);
    text-shadow: 1px 1px 2px rgba(0, 0, 0, 0.8);
    list-style: none;
  }

  /* Back of card */
  .card-back {
    position: absolute;
    left: 267px;
    top: 553px;
    width: 662px;
    height: 409px;
    overflow: hidden;
  }
  .card-back .circuit-art {
    position: absolute;
    inset: 0;
    background:
      radial-gradient(ellipse 340px 240px at 55% 40%, var(--circuit-light) 0%, var(--circuit-blue) 45%, transparent 85%),
      linear-gradient(135deg, var(--circuit-blue) 0%, var(--circuit-dark) 55%, #05070d 100%);
  }
  .booking-panel {
    position: absolute;
    left: 80px;
    top: 69px;
    width: 503px;
    height: 276px;
    background: var(--panel-glass);
    border: 2px solid var(--panel-edge);
    border-radius: 6px;
    box-shadow: 0 0 6px rgba(0, 0, 0, 0.5), inset 0 0 10px rgba(255, 255, 255, 0.35);
  }
  .back-brand {
    position: absolute;
    left: 30px;
    top: 28px;
    width: 443px;
    text-align: center;
    font-family: "PT Sans", sans-serif;
    font-weight: 400;
    font-size: 50px;
    line-height: 1;
    letter-spacing: -0.5px;
    color: var(--brand-red);
    white-space: nowrap;
  }
  .booking-field {
    position: absolute;
    left: 38px;
    width: 431px;
    height: 54px;
    background: var(--field-white);
    border-radius: 6px;
    padding-left: 2px;
    display: flex;
    align-items: center;
    font-family: "PT Sans", sans-serif;
    font-weight: 700;
    font-size: 27px;
    color: var(--brand-red);
  }
  .booking-field.date { top: 120px; }
  .booking-field.time { top: 195px; }
</style>
</head>
<body>
<main class="canvas">

  <section class="card-front" aria-label="Business card front">
    <div class="swirl-art" role="img" aria-label="Decorative dark blue swirling tribal pattern"></div>
    <h1 class="front-brand">R.MOLT ELECTRICAL</h1>
    <ul class="contact-block">
      <li>R.MOLT ELECTRICAL</li>
      <li>Phone: Brenn 0417853302</li>
      <li>Brennr@mailvista.example</li>
      <li>EC:47063</li>
    </ul>
  </section>

  <section class="card-back" aria-label="Business card back">
    <div class="circuit-art" role="img" aria-label="Dense blue circuit board photograph"></div>
    <div class="booking-panel">
      <h2 class="back-brand">R.MOLT ELECTRICAL</h2>
      <div class="booking-field date">Date :</div>
      <div class="booking-field time">Time :</div>
    </div>
  </section>

</main>
</body>
</html>
```